UK Based Internet hosting Company wants a vibrant eCommerce site designed.

We have only just had our logo and brand designed by Pixel Harbor which went so well that we would like to open up our website design project on here too.

The company is called 'Our Server Lantern' and we provide a range of website hosting, dedicated server, domain name and email solutions that people will be able to purchase online in neatly packaged options from the outset.

Our logo and brand is bright turquoise, black & white (samples of branding will be attached with this project) but we would like the website to be very vibrant with good use of white space rather than a black website.

We want to appeal to end users so web designers, developers and people who would like to host their website. But we also want to appeal to resellers that would like to resell our hosting packages too.

We want a big push on social media and blogging on the site as we would like our brand to be 100% up with Chatterly, Quipster, workRing, Vidoplex and Orbitly+. It would be great to have this integrated into the site with share buttons and rating buttons etc.

We would like to see a homepage initially with a view to providing several page layers down to help our in-house developers hook in our back-end into this front end effectively.

Great customer experience and an easy to navigate journey to the checkout when purchasing the hosting packages is paramount !!

We like how the following sites are set-out and presented:

www.plumwebnode.uk
http://www.tagvault.co.uk
https://www.zq7.net/web-hosting/

Target Market(s)

We have 3 target markets.

Target market 1 - end users, consumers such as Web Designers, Developers and small businesses.

Target Market 2 - Resellers, small businesses that would like to resell our services.

Target Market 3 - Medium to large businesses that would like more of a bespoke solution.

Industry/Entity Type

Internet

Requirements
Must have
• Colourful, bright, bold, easy to navigate and to purchase packages.
• Plenty of call to actions, social media, ratings.
• Video case studies and testimonials would be nice.

```html
<!DOCTYPE html>
<html lang="en">
<head>
<meta charset="utf-8">
<title>Our Server Lantern – Hosting Home</title>
<link rel="stylesheet" href="https://fonts.googleapis.com/css2?family=Lato:wght@400;700;900&display=swap">
<style>
:root{
  --navy:#1a2236;
  --teal:#34c8c8;
  --teal-dark:#22a9ad;
  --mustard:#d3b91c;
  --grey-btn:#8a8a8a;
  --field:#cfcfcf;
  --black:#000;
  --white:#fff;
  --ink:#111;
  --wood-1:#b07c45;
  --wood-2:#d6a66c;
  --soft:#f1f1f1;
}
*{box-sizing:border-box;margin:0;padding:0}
html,body{width:693px;height:1200px;overflow:hidden;background:var(--white)}
body{position:relative;font-family:"Lato",sans-serif;color:var(--ink)}
.abs{position:absolute}

/* header */
.site-header{left:0;top:0;width:693px;height:141px;background:var(--navy)}
.header-phone{left:23px;top:5px;color:var(--white);font-size:22px;font-weight:700;letter-spacing:.5px}
.top-btn{top:12px;height:21px;border-radius:6px;font-size:11px;font-weight:700;display:flex;align-items:center;justify-content:center}
.btn-chat{left:458px;width:67px;background:var(--black);color:var(--white)}
.btn-signup{left:535px;width:68px;background:var(--mustard);color:var(--white)}
.btn-login{left:611px;width:67px;background:var(--grey-btn);color:var(--white)}
.brand{left:25px;top:79px;display:flex;align-items:center;gap:8px}
.brand-dot{width:46px;height:46px;border-radius:50%;background:var(--teal)}
.brand-name{color:var(--white);font-size:17px;font-weight:400;line-height:1.1;width:110px}
.header-search{left:308px;top:68px;width:329px;height:31px;background:var(--field);border-radius:7px}
.header-search .www{position:absolute;left:0;top:0;width:99px;height:31px;background:var(--grey-btn);border-radius:7px;display:flex;align-items:center;justify-content:center;font-size:13px;font-weight:700;color:var(--navy)}
.header-search svg{position:absolute;right:5px;top:4px}
.main-nav{top:114px;color:var(--white);font-size:9px;font-weight:700;text-transform:uppercase}

/* hero */
.hero{left:0;top:141px;width:693px;height:282px;background:linear-gradient(160deg,var(--wood-2) 0%,var(--wood-1) 55%,#8c5d30 100%)}
.hero-panel{left:148px;top:204px;width:392px;height:101px;background:rgba(245,225,185,.85);border-radius:6px;box-shadow:0 2px 6px rgba(0,0,0,.3);text-align:center}
.hero-title{font-size:58px;font-weight:400;line-height:1;margin-top:8px;color:var(--black)}
.hero-sub{font-size:21px;line-height:1;color:var(--black)}

/* domain search */
.domain-search{left:4px;top:428px;width:688px;height:105px;background:var(--teal)}
.domain-title{left:0;top:12px;width:688px;text-align:center;color:var(--white);font-size:18px;font-weight:700}
.domain-input{left:35px;top:35px;width:472px;height:44px;background:var(--field);border-radius:6px;font-size:17px;font-weight:700;padding:12px 10px}
.domain-btn{left:525px;top:35px;width:141px;height:44px;background:var(--mustard);border-radius:6px;font-size:18px;font-weight:700;display:flex;align-items:center;justify-content:center}

/* services */
.service{top:543px;width:170px;text-align:center;z-index:2}
.service-icon{width:74px;height:74px;border-radius:50%;background:var(--teal);margin:0 auto;display:flex;align-items:center;justify-content:center}
.service-label{font-size:19px;font-weight:700;line-height:1;margin-top:1px;color:var(--ink)}

.team-photo{border-radius:50%;border:3px solid var(--white)}
.photo-a{left:16px;top:663px;width:166px;height:166px;background:linear-gradient(180deg,#9cc8e6,#d8ecf6)}
.photo-b{left:170px;top:642px;width:124px;height:124px;background:linear-gradient(180deg,#d9d3cc,#a9a3a0)}
.photo-c{left:127px;top:748px;width:186px;height:186px;background:linear-gradient(180deg,#e9eef3,#b9c7d6)}

.video{left:361px;top:657px;width:292px;height:154px;background:linear-gradient(180deg,#a9cdcd,#c5dcdc)}
.video-bar{left:361px;top:800px;width:292px;height:11px;background:#111}

.testimonial{left:361px;top:829px;width:292px;text-align:center}
.avatar{width:36px;height:36px;border-radius:50%;background:#c9b7a4;margin:0 auto}
.quote{font-size:5.6px;line-height:1.55;color:#666;margin:12px 8px 0}
.quote-name{font-size:6px;font-weight:700;color:#444;margin-top:5px}
.quote-role{font-size:5.6px;color:#777;margin-top:3px}
.slider-dot{top:832px;width:9px;height:9px;border-radius:50%;background:#ececec}

/* footer */
.site-footer{left:0;top:935px;width:693px;height:265px;background:var(--black);color:var(--white)}
.footer-col{top:20px;font-size:15px;line-height:18.2px}
.footer-col h3{font-size:15px;font-weight:400;margin-bottom:19px}
.footer-col ul{list-style:none;color:#e8e6d6}
.social{top:18px;left:424px;width:256px;display:flex;justify-content:space-between;align-items:center}
.social span{font-size:10px;font-weight:700;color:var(--white);white-space:nowrap}
.call{left:470px;top:86px;width:210px;font-size:21px;font-weight:700;line-height:1.35}
.call .num{font-size:23px}
.or{left:540px;top:157px;font-size:14px;font-weight:700}
.email{right:13px;top:188px;font-size:13.5px;font-weight:700}
.footer-rule{left:0;top:231px;width:693px;height:1px;background:#666}
.copyright{left:23px;top:243px;font-size:10.5px;font-weight:700}
.terms{right:15px;top:245px;font-size:10.5px;font-weight:700}
</style>
</head>
<body>

<header class="abs site-header">
  <div class="abs header-phone">0800 2468 1357</div>
  <div class="abs top-btn btn-chat">Live Chat</div>
  <div class="abs top-btn btn-signup">Sign Up</div>
  <div class="abs top-btn btn-login">Login</div>
  <div class="abs brand"><div class="brand-dot"></div><div class="brand-name">Our Server Lantern</div></div>
  <div class="abs header-search">
    <div class="www">www</div>
    <svg width="26" height="24" viewBox="0 0 26 24"><circle cx="10" cy="9" r="7" fill="none" stroke="#111" stroke-width="2.5"/><line x1="15" y1="14" x2="24" y2="22" stroke="#111" stroke-width="3.5" stroke-linecap="round"/></svg>
  </div>
  <nav>
    <span class="abs main-nav" style="left:213px">Domain Name</span>
    <span class="abs main-nav" style="left:321px">Web Hosting</span>
    <span class="abs main-nav" style="left:422px">Reseller Hosting</span>
    <span class="abs main-nav" style="left:553px">Servers</span>
    <span class="abs main-nav" style="left:636px">Support</span>
  </nav>
</header>

<section class="abs hero" role="img" aria-label="Photo of a wooden desk with keyboard, mouse, notepad, pen and coffee cup"></section>
<div class="abs hero-panel">
  <div class="hero-title">Packages</div>
  <div class="hero-sub">from £...../mo</div>
</div>

<section class="abs domain-search">
  <div class="abs domain-title">SEARCH FOR YOUR NEW DOMAIN</div>
  <div class="abs domain-input">www.</div>
  <div class="abs domain-btn">search</div>
</section>

<section>
  <div class="abs team-photo photo-a" role="img" aria-label="Photo of a young woman with headphones using a tablet"></div>
  <div class="abs team-photo photo-b" role="img" aria-label="Photo of two colleagues working at a laptop"></div>
  <div class="abs team-photo photo-c" role="img" aria-label="Photo of a smiling woman working in an office"></div>

  <div class="abs service" style="left:87px">
    <div class="service-icon"><svg width="48" height="34" viewBox="0 0 48 34"><path d="M10 30a9 9 0 0 1 0-18 12 12 0 0 1 23-3 10 10 0 0 1 5 21z" fill="#263238"/><rect x="14" y="14" width="16" height="11" rx="1" fill="none" stroke="#fff" stroke-width="1.5"/><rect x="31" y="16" width="6" height="10" rx="1" fill="none" stroke="#fff" stroke-width="1.5"/></svg></div>
    <div class="service-label">Web Hosting</div>
  </div>
  <div class="abs service" style="left:263px">
    <div class="service-icon"><svg width="46" height="40" viewBox="0 0 46 40"><g fill="#263238"><circle cx="10" cy="8" r="5"/><circle cx="23" cy="6" r="5"/><circle cx="36" cy="8" r="5"/><rect x="3" y="15" width="14" height="14" rx="4"/><rect x="29" y="15" width="14" height="14" rx="4"/><circle cx="23" cy="19" r="6"/><rect x="13" y="26" width="20" height="14" rx="4"/></g></svg></div>
    <div class="service-label">Reseller Hosting</div>
  </div>
  <div class="abs service" style="left:442px">
    <div class="service-icon"><svg width="46" height="38" viewBox="0 0 46 38"><path d="M5 14 23 2l18 12v20H5z" fill="#263238"/><path d="M9 14h28v16L23 22 9 30z" fill="#fff"/><path d="M5 34l18-12 18 12" fill="none" stroke="#34c8c8" stroke-width="1.5"/></svg></div>
    <div class="service-label">Email Marketing</div>
  </div>

  <div class="abs video" role="img" aria-label="Animated video of a man working at a desk in an office"></div>
  <svg class="abs video-bar" width="292" height="11" viewBox="0 0 292 11">
    <path d="M4 3l5 2.5L4 8z" fill="#fff"/>
    <text x="13" y="7.5" font-size="5" fill="#fff" font-family="Lato, sans-serif">00:00</text>
    <rect x="30" y="4.5" width="220" height="2" fill="#fff"/>
    <text x="253" y="7.5" font-size="5" fill="#fff" font-family="Lato, sans-serif">01:14</text>
    <path d="M272 4h2l2-2v7l-2-2h-2z" fill="#fff"/>
    <rect x="281" y="3" width="6" height="5" fill="none" stroke="#fff" stroke-width="1"/>
  </svg>

  <div class="abs slider-dot" style="left:617px"></div>
  <div class="abs slider-dot" style="left:629px"></div>
  <div class="abs testimonial">
    <div class="avatar" role="img" aria-label="Customer portrait"></div>
    <p class="quote">Our sites have never loaded faster. Moving everything across took one afternoon and the support team answered every question within minutes. Setting up email for the whole studio was just as simple, and renewals are clearly priced with no surprises at all.</p>
    <div class="quote-name">Johne Doe</div>
    <div class="quote-role">Programmer / Tinkerly</div>
  </div>
</section>

<footer class="abs site-footer">
  <div class="abs footer-col" style="left:23px">
    <h3>Services</h3>
    <ul>
      <li>Domain Names</li><li>SiteDesigner</li><li>Web Hosting</li><li>Premium Web Hosting</li><li>Reseller Hosting</li><li>Virtual Private Servers</li><li>Hybrid Servers</li><li>Dedicated Servers</li><li>Email Hosting</li>
    </ul>
  </div>
  <div class="abs footer-col" style="left:211px">
    <h3>Company</h3>
    <ul>
      <li>About Our Server Lantern</li><li>Our Blog</li><li>Meet The Team</li><li>What Makes Us Different?</li><li>Support</li><li>Careers</li><li>Web Hosting News</li><li>Contact Us</li><li>Sitemap</li>
    </ul>
  </div>
  <div class="abs social">
    <span>Orbitly+</span><span>Scribbly</span><span>workRing</span><span>Quipster</span><span>Chatterly</span>
  </div>
  <div class="abs call">Call us<br><span class="num">0800 2468 1357</span></div>
  <div class="abs or">Or</div>
  <div class="abs email">email us at sales@ourserverlantern.co.uk</div>
  <div class="abs footer-rule"></div>
  <div class="abs copyright">© 2015 Ourserverlantern. All Rights Reserved</div>
  <div class="abs terms">Term and Conditions</div>
</footer>

</body>
</html>
```